Senior Care and Care home flyer

We are getting ready to advertise with a company called "CoupTrek" and our advertisement includes a 3"x8" DOUBLE SIDED insert. Live Area: This is the maximum size of your page content. (Coupon: 3" x 7.9167")
Both sides should have
Address: 4837 Lunalilo Ave. Suite 612 Honolulu, HI 96814
Phone: 808-555-2719
Website: www.HarperCare.com
-We would like a space for a QR code on both sides

1 side : make color scheme that blue from the last one
Harper Care Group: featuring Harper Senior Living
Logo for Senior Living
Harper Care Group can provide care to your loved ones in our home-Harper Senior Living Kailua. Clients and their families can experience Harper's culture of heart-centered, compassionate care in their own home... or in ours.
Senior Living Benefits/Features:
19 Fully Furnished Suites
Meals, Laundry, Housekeeping
Activities & Transportation
On-site 24/7 Care Services
Some items to include on flyer.
Schedule Tour today

Side 2: make the color scheme that green from the last flyer
Harper Care Group: Featuring Harper Homecare
Logo for HomeCare
General information for Harper Care group:
Harper Care Group has been providing homecare to Oahu's Kupuna for the past 26 years. Harper Homecare offers personal care services to meet your loved one's needs in the comfort and safety of their own home.
Homecare Services:
Home Health Aides
Skilled Nursing
Bath & Meal Service
Medication Management
Services Available 24/7

Target Market for Side 2: Ages 55-105 Males and Females, looking for care or a home for themselves or their loved ones
-Complimentary Care Consultation
Maybe homecare side says in your home and senior living side said or ours.
Include on both sides
-25+ Years in business
-Locally owned and operated
-Licensed and Insured

Flyer should be 3"x8" DOUBLE SIDED horizontal/landscape/please utilize information that you have used on past ads as a guide.

Industry/Entity Type

Home Health Care Senior Living

Colors
0094D4
00A9DD
6FCCEA
C7EBF8
E9F6FB
00AB8E
00BBA5
67D7C9
C6EFE9
E9F9F6

Requirements
Must have
• Live Area: This is the maximum size of your page content. (Coupon: 3" x 7.9167")
Should not have
• NO PINK OR PEACH colors

```html
<!DOCTYPE html>
<html lang="en">
<head>
<meta charset="utf-8">
<title>Harper Care Group – Insert Cards</title>
<link href="https://fonts.googleapis.com/css2?family=Allura&family=Fira+Sans:ital,wght@0,400;0,500;0,700;1,400;1,500&family=Fira+Sans+Condensed:wght@400;500;700;800&display=swap" rel="stylesheet">
<style>
  :root{
    --stage:#454545;
    --white:#ffffff;
    --ink:#4a4a4a;
    --blue:#3b87a1;
    --slate:#676767;
    --teal:#00786c;
    --green:#00ab8e;
    --green-soft:#67d7c9;
    --qr-line:#c9c9c9;
  }
  *{margin:0;padding:0;box-sizing:border-box}
  html,body{width:1200px;height:1003px;overflow:hidden;background:var(--stage)}
  body{position:relative;font-family:"Fira Sans",sans-serif;color:var(--ink)}

  .card{position:absolute;width:846px;height:317px;background:var(--white);overflow:hidden}
  .card--living{left:119px;top:139px;--accent:var(--blue);--head:var(--slate);--icon:var(--blue)}
  .card--homecare{left:217px;top:547px;--accent:var(--teal);--head:var(--green);--icon:var(--green)}

  .card__art{position:absolute;inset:0;width:846px;height:317px}

  .brand{position:absolute;display:flex;flex-direction:column;align-items:center;transform:translateX(-50%)}
  .brand__mark{width:30px;height:30px;background:var(--accent);border-radius:6px;margin-bottom:8px}
  .brand__name{font-family:"Fira Sans",sans-serif;font-weight:500;color:var(--accent);font-size:21px;line-height:1.05;text-align:center}
  .brand__sub{font-family:"Fira Sans",sans-serif;font-weight:500;color:var(--accent);font-size:8px;letter-spacing:5px;margin-top:3px}

  .intro{position:absolute;width:262px;transform:translateX(-50%);text-align:center;font-size:9.4px;line-height:12.3px;color:var(--ink)}

  .credential{position:absolute;transform:translateX(-50%);display:flex;flex-direction:column;align-items:center;text-align:center;font-family:"Fira Sans Condensed",sans-serif;font-size:8.2px;line-height:10.5px;letter-spacing:.3px;color:var(--ink);text-transform:uppercase}
  .credential svg{margin-bottom:8px}
  .credential-divider{position:absolute;width:1px;height:50px;background:#bdbdbd}

  .tagline-script{position:absolute;font-family:"Allura",cursive;color:var(--accent);font-size:21px;line-height:24px;white-space:nowrap}
  .tagline-bold{position:absolute;transform:translateX(-50%);font-family:"Fira Sans Condensed",sans-serif;font-weight:700;color:var(--accent);font-size:13.5px;white-space:nowrap}

  .qr-space{position:absolute;width:94px;height:94px;background:var(--white);border:1px solid var(--qr-line)}

  .feature-box{position:absolute;background:var(--white);border:1px solid var(--white)}
  .feature-box__head{background:var(--head);color:var(--white);font-family:"Fira Sans Condensed",sans-serif;font-weight:700;font-size:13px;height:23px;line-height:23px;padding-left:8px;letter-spacing:.2px}
  .feature-box__list{list-style:none}
  .feature-box__item{display:flex;align-items:center;gap:7px;padding-left:7px;height:22px;font-size:12.4px;color:var(--ink);border-top:1px solid var(--accent)}
  .feature-box__item:first-child{border-top:none}
  .feature-box__item svg{flex:none}

  .cta{position:absolute;color:var(--white)}
  .cta__lead{font-family:"Fira Sans",sans-serif;font-style:italic;font-weight:500;font-size:20px;line-height:22px}
  .cta__phone{font-family:"Fira Sans Condensed",sans-serif;font-weight:800;font-size:29.5px;line-height:30px;letter-spacing:.2px}
  .cta__web{display:inline-block;background:var(--white);color:var(--accent);border-radius:10px;font-size:11.5px;letter-spacing:2.6px;height:18px;line-height:18px;padding:0 10px;margin-top:3px}
  .cta__web b{font-weight:700}
  .cta__address{display:flex;align-items:flex-start;gap:7px;margin-top:6px;font-family:"Fira Sans Condensed",sans-serif;font-size:9.6px;line-height:11px;padding-left:6px}
</style>
</head>
<body>

<!-- Side 1 : Senior Living -->
<section class="card card--living" aria-label="Harper Senior Living insert">
  <svg class="card__art" viewBox="0 0 846 317">
    <defs>
      <linearGradient id="living-photo-tone" x1="0" y1="0" x2="1" y2="1">
        <stop offset="0" stop-color="#e9d9a8"/>
        <stop offset=".45" stop-color="#5a8fc7"/>
        <stop offset="1" stop-color="#c9823f"/>
      </linearGradient>
      <linearGradient id="living-bedroom-tone" x1="0" y1="0" x2="1" y2="1">
        <stop offset="0" stop-color="#d8c4a3"/><stop offset="1" stop-color="#7a4a32"/>
      </linearGradient>
      <linearGradient id="living-dining-tone" x1="0" y1="0" x2="1" y2="1">
        <stop offset="0" stop-color="#c9a57a"/><stop offset="1" stop-color="#5a2a1c"/>
      </linearGradient>
    </defs>
    <path role="img" aria-label="Photo: caregiver in blue scrubs chatting with a resident on a living room sofa" d="M0,0 H292 C330,80 318,200 180,317 H0 Z" fill="url(#living-photo-tone)"/>
    <path d="M300,0 C340,80 325,200 185,317" fill="none" stroke="var(--blue)" stroke-width="6"/>
    <circle role="img" aria-label="Photo: furnished resident suite bedroom" cx="272" cy="160" r="43" fill="url(#living-bedroom-tone)" stroke="#fff" stroke-width="4"/>
    <circle role="img" aria-label="Photo: shared dining room" cx="210" cy="254" r="48" fill="url(#living-dining-tone)" stroke="#fff" stroke-width="4"/>
    <path d="M650,0 H846 V317 H540 C545,290 575,278 608,262 C620,250 616,220 640,196 L760,60 Z" fill="var(--blue)"/>
    <path d="M628,0 L660,0 L695,45 L680,45 Z" fill="#5e5e5e"/>
    <path d="M652,147 C640,175 625,195 610,205" fill="none" stroke="#5e5e5e" stroke-width="3"/>
  </svg>

  <div class="brand" style="left:436px;top:14px">
    <span class="brand__mark"></span>
    <span class="brand__name">Harper<br>Senior Living</span>
    <span class="brand__sub">KAILUA</span>
  </div>

  <p class="intro" style="left:457px;top:117px">Harper Senior Living provides around the clock care for your loved ones in our home, Harper Senior Living Kailua. Our residents receive assistance with daily living activities, medication management, and personal care focused on individual needs.</p>

  <div class="credential" style="left:322px;top:188px">
    <svg width="30" height="32" viewBox="0 0 30 32" fill="none" stroke="var(--icon)" stroke-width="1.3"><path d="M2 30H28M4 30V24H10V18H16V12H22V30"/><path d="M20 12V2L26 4L20 6"/></svg>
    <span>25+ Years<br>In Business</span>
  </div>
  <span class="credential-divider" style="left:361px;top:196px"></span>
  <div class="credential" style="left:408px;top:188px">
    <svg width="36" height="32" viewBox="0 0 36 32" fill="none" stroke="var(--icon)" stroke-width="1.3"><path d="M3 12L6 5H24L27 12Z"/><path d="M5 12V30H25V12"/><rect x="8" y="17" width="7" height="6"/><rect x="17" y="17" width="5" height="13"/><circle cx="29" cy="7" r="5"/><circle cx="29" cy="7" r="1.6"/></svg>
    <span>Woman Service-<br>Disabled Veteran-<br>Owned &amp; Operated<br>Small Business</span>
  </div>
  <span class="credential-divider" style="left:454px;top:196px"></span>
  <div class="credential" style="left:485px;top:188px">
    <svg width="34" height="32" viewBox="0 0 34 32" fill="none" stroke="var(--icon)" stroke-width="1.3"><rect x="3" y="8" width="18" height="22"/><path d="M6 14H14M6 19H12M6 24H16"/><path d="M24 2L32 5V12C32 17 28 20 24 22C20 20 16 17 16 12V5Z" fill="#fff"/><path d="M20 11L23 14L28 8"/></svg>
    <span>Licensed &amp;<br>Insured</span>
  </div>

  <span class="tagline-script" style="left:306px;top:280px">More Than Assisted Living</span>

  <div class="qr-space" style="left:523px;top:202px" aria-label="QR code space"></div>

  <div class="feature-box" style="left:599px;top:30px;width:219px">
    <div class="feature-box__head">BENEFITS OF SENIOR LIVING</div>
    <ul class="feature-box__list">
      <li class="feature-box__item"><svg width="10" height="10" viewBox="0 0 10 10" fill="none" stroke="var(--blue)" stroke-width="1.1"><rect x=".5" y=".5" width="9" height="9"/><path d="M2.5 5L4.5 7L8 3"/></svg>19 Fully Furnished Suites</li>
      <li class="feature-box__item"><svg width="10" height="10" viewBox="0 0 10 10" fill="none" stroke="var(--blue)" stroke-width="1.1"><rect x=".5" y=".5" width="9" height="9"/><path d="M2.5 5L4.5 7L8 3"/></svg>Meals, Laundry, Housekeeping</li>
      <li class="feature-box__item"><svg width="10" height="10" viewBox="0 0 10 10" fill="none" stroke="var(--blue)" stroke-width="1.1"><rect x=".5" y=".5" width="9" height="9"/><path d="M2.5 5L4.5 7L8 3"/></svg>Activities &amp; Transportation</li>
      <li class="feature-box__item"><svg width="10" height="10" viewBox="0 0 10 10" fill="none" stroke="var(--blue)" stroke-width="1.1"><rect x=".5" y=".5" width="9" height="9"/><path d="M2.5 5L4.5 7L8 3"/></svg>On-site 24/7 Care Services</li>
    </ul>
  </div>

  <div class="cta" style="left:626px;top:199px">
    <div class="cta__lead">Schedule tour today</div>
    <div class="cta__phone">808-555-2719</div>
    <div class="cta__web">WWW.<b>HARPERCARE</b>.COM</div>
    <div class="cta__address">
      <svg width="8" height="11" viewBox="0 0 8 11"><path d="M4 0C1.8 0 0 1.8 0 4C0 7 4 11 4 11C4 11 8 7 8 4C8 1.8 6.2 0 4 0Z" fill="#fff"/><circle cx="4" cy="4" r="1.5" fill="var(--blue)"/></svg>
      <span>2150 Mokapu Rd, Kailua, HI 96734</span>
    </div>
  </div>
</section>

<!-- Side 2 : Homecare -->
<section class="card card--homecare" aria-label="Harper Homecare insert">
  <svg class="card__art" viewBox="0 0 846 317">
    <defs>
      <linearGradient id="home-photo-tone" x1="0" y1="0" x2="1" y2="1">
        <stop offset="0" stop-color="#5a5f72"/>
        <stop offset=".5" stop-color="#b99a88"/>
        <stop offset="1" stop-color="#3b3550"/>
      </linearGradient>
      <linearGradient id="home-veteran-tone" x1="0" y1="0" x2="1" y2="1">
        <stop offset="0" stop-color="#e6e4de"/><stop offset="1" stop-color="#6b6a52"/>
      </linearGradient>
      <linearGradient id="home-family-tone" x1="0" y1="0" x2="1" y2="1">
        <stop offset="0" stop-color="#efece8"/><stop offset="1" stop-color="#4b3a36"/>
      </linearGradient>
    </defs>
    <path role="img" aria-label="Photo: caregiver's hand resting on an elderly woman's shoulder" d="M0,0 H292 C325,80 320,200 180,317 H0 Z" fill="url(#home-photo-tone)"/>
    <path d="M300,0 C338,80 325,200 185,317" fill="none" stroke="var(--teal)" stroke-width="6"/>
    <circle role="img" aria-label="Photo: veteran in a wheelchair at home" cx="272" cy="157" r="42" fill="url(#home-veteran-tone)" stroke="#fff" stroke-width="4"/>
    <circle role="img" aria-label="Photo: mother fitting a mask on her daughter" cx="211" cy="254" r="47" fill="url(#home-family-tone)" stroke="#fff" stroke-width="4"/>
    <path d="M650,0 H846 V317 H540 C545,290 575,278 608,262 C620,250 616,220 640,196 L760,60 Z" fill="var(--teal)"/>
    <path d="M622,0 L644,0 L680,45 L665,45 Z" fill="var(--green-soft)"/>
    <path d="M636,168 C625,190 615,200 608,208" fill="none" stroke="var(--green-soft)" stroke-width="3"/>
  </svg>

  <div class="brand" style="left:451px;top:16px">
    <span class="brand__mark"></span>
    <span class="brand__name" style="font-size:26px">Harper</span>
    <span class="brand__sub" style="font-size:9px">HOMECARE</span>
  </div>

  <p class="intro" style="left:454px;top:118px;width:252px">Harper Homecare has been providing personalized home care to Oahu's kupuna to keiki for over 25 years. Our clients receive a wide range of individual care services from assistance with daily living activities to skilled nursing care and Alzheimer's assisted living in the comfort and sanctuary of your own home.</p>

  <div class="credential" style="left:320px;top:200px">
    <svg width="30" height="32" viewBox="0 0 30 32" fill="none" stroke="var(--icon)" stroke-width="1.3"><path d="M2 30H28M4 30V24H10V18H16V12H22V30"/><path d="M20 12V2L26 4L20 6"/></svg>
    <span>25+ Years<br>In Business</span>
  </div>
  <span class="credential-divider" style="left:352px;top:208px"></span>
  <div class="credential" style="left:406px;top:200px">
    <svg width="36" height="32" viewBox="0 0 36 32" fill="none" stroke="var(--icon)" stroke-width="1.3"><path d="M3 12L6 5H24L27 12Z"/><path d="M5 12V30H25V12"/><rect x="8" y="17" width="7" height="6"/><rect x="17" y="17" width="5" height="13"/><circle cx="29" cy="7" r="5"/><circle cx="29" cy="7" r="1.6"/></svg>
    <span>Woman Service-<br>Disabled Veteran-<br>Owned &amp; Operated<br>Small Business</span>
  </div>
  <span class="credential-divider" style="left:453px;top:208px"></span>
  <div class="credential" style="left:485px;top:200px">
    <svg width="34" height="32" viewBox="0 0 34 32" fill="none" stroke="var(--icon)" stroke-width="1.3"><rect x="3" y="8" width="18" height="22"/><path d="M6 14H14M6 19H12M6 24H16"/><path d="M24 2L32 5V12C32 17 28 20 24 22C20 20 16 17 16 12V5Z" fill="#fff"/><path d="M20 11L23 14L28 8"/></svg>
    <span>Licensed &amp;<br>Insured</span>
  </div>

  <span class="tagline-bold" style="left:396px;top:286px">Call for Complimentary Consultation</span>

  <div class="qr-space" style="left:523px;top:203px" aria-label="QR code space"></div>

  <div class="feature-box" style="left:599px;top:30px;width:214px">
    <div class="feature-box__head">HOMECARE SERVICES</div>
    <ul class="feature-box__list">
      <li class="feature-box__item"><svg width="10" height="10" viewBox="0 0 10 10" fill="none" stroke="var(--teal)" stroke-width="1.1"><rect x=".5" y=".5" width="9" height="9"/><path d="M2.5 5L4.5 7L8 3"/></svg>Personal Care Services</li>
      <li class="feature-box__item"><svg width="10" height="10" viewBox="0 0 10 10" fill="none" stroke="var(--teal)" stroke-width="1.1"><rect x=".5" y=".5" width="9" height="9"/><path d="M2.5 5L4.5 7L8 3"/></svg>Home Aides &amp; Nurses</li>
      <li class="feature-box__item"><svg width="10" height="10" viewBox="0 0 10 10" fill="none" stroke="var(--teal)" stroke-width="1.1"><rect x=".5" y=".5" width="9" height="9"/><path d="M2.5 5L4.5 7L8 3"/></svg>Bath &amp; Meal Service</li>
      <li class="feature-box__item"><svg width="10" height="10" viewBox="0 0 10 10" fill="none" stroke="var(--teal)" stroke-width="1.1"><rect x=".5" y=".5" width="9" height="9"/><path d="M2.5 5L4.5 7L8 3"/></svg>Medication Management</li>
      <li class="feature-box__item"><svg width="10" height="10" viewBox="0 0 10 10" fill="none" stroke="var(--teal)" stroke-width="1.1"><rect x=".5" y=".5" width="9" height="9"/><path d="M2.5 5L4.5 7L8 3"/></svg>Services Available 24/7</li>
    </ul>
  </div>

  <div class="cta" style="left:625px;top:200px">
    <div class="cta__lead">Call Us Today</div>
    <div class="cta__phone">808-555-2719</div>
    <div class="cta__web">WWW.<b>HARPERCARE</b>.COM</div>
    <div class="cta__address">
      <svg width="10" height="14" viewBox="0 0 8 11"><path d="M4 0C1.8 0 0 1.8 0 4C0 7 4 11 4 11C4 11 8 7 8 4C8 1.8 6.2 0 4 0Z" fill="#fff"/><circle cx="4" cy="4" r="1.5" fill="var(--teal)"/></svg>
      <span>4837 Lunalilo Ave. Suite 612<br>Honolulu, HI 96814</span>
    </div>
  </div>
</section>

</body>
</html>
```